Brovanix Stationery Design Project

We need a stationery design for our new business Brovanix which deals in advanced cleaning technologies such as Ultrasonic cleaning and high pressure cleaning machinery.

Our colour scheme is as per the included files.

We require business cards, letterheads, a brochure folder and email signatures design
Updates

Apologies for the delay in making a decision on this project. We will be making a final decision during the course of next week

Target Market(s)

Industries ranging from medical, automotive, mining, engineering all requiring specialised cleaning services

Industry/Entity Type

Pressure Cleaning

Requirements
Must have
• Please include our supplied logo and colour scheme. The design needs to be professional but creative.

```html
<!DOCTYPE html>
<html lang="en">
<head>
<meta charset="utf-8">
<title>Brovanix Business Card</title>
<link href="https://fonts.googleapis.com/css2?family=PT+Sans:wght@400;700&display=swap" rel="stylesheet">
<style>
  :root {
    --backdrop: #dfe4e8;
    --card: #ffffff;
    --navy: #2f3f8f;
    --royal: #3b4fa0;
    --grey: #8a8a8a;
    --grey-dark: #707070;
    --shadow: rgba(20, 35, 50, 0.18);
  }
  * { margin: 0; padding: 0; box-sizing: border-box; }
  html, body {
    width: 1200px; height: 960px; overflow: hidden;
    background: var(--backdrop);
    font-family: "PT Sans", Arial, sans-serif;
  }
  .stage { position: relative; width: 1200px; height: 960px; }
  .card {
    position: absolute; left: 300px; width: 600px; height: 340px;
    background: var(--card);
    box-shadow: 0 10px 30px var(--shadow);
    overflow: hidden;
  }
  .card--front { top: 70px; }
  .card--back { top: 520px; }

  /* Front */
  .brand { position: absolute; left: 62px; top: 64px; display: flex; align-items: center; gap: 16px; }
  .brand__square { width: 62px; height: 62px; background: var(--royal); }
  .brand__name { font-size: 50px; font-weight: 700; color: var(--grey); letter-spacing: 2px; line-height: 1; text-transform: uppercase; }
  .brand__tagline { position: absolute; left: 140px; top: 122px; font-size: 19px; color: var(--royal); }
  .contact {
    position: absolute; left: 190px; top: 188px;
    border-left: 3px solid var(--navy);
    padding-left: 12px;
    color: var(--grey-dark);
    font-size: 13.5px; line-height: 1.55;
  }
  .contact__name { font-size: 24px; color: var(--grey); line-height: 1.2; margin-bottom: 8px; }
  .contact__role { font-size: 14px; margin-left: 8px; }
  .contact__label { display: inline-block; width: 18px; font-weight: 700; color: var(--navy); }
  .contact__web strong { color: var(--navy); }

  /* Back */
  .back__field {
    position: absolute; left: 0; top: 0; width: 450px; height: 340px;
    background: linear-gradient(135deg, #2e3f8c, #4559a8);
  }
  .back__strip {
    position: absolute; right: 0; top: 0; width: 150px; height: 340px;
    display: flex; align-items: center; justify-content: center; gap: 4px;
    writing-mode: vertical-rl; transform: rotate(180deg);
  }
  .back__name { font-size: 48px; font-weight: 700; color: var(--grey); letter-spacing: 2px; text-transform: uppercase; line-height: 1; }
  .back__tagline { font-size: 15px; color: var(--grey-dark); }
</style>
</head>
<body>
<main class="stage">
  <section class="card card--front">
    <div class="brand">
      <span class="brand__square"></span>
      <span class="brand__name">Brovanix</span>
    </div>
    <p class="brand__tagline">Advanced Cleaning Technologies</p>
    <div class="contact">
      <p class="contact__name">Andres Valmar<span class="contact__role">Manager</span></p>
      <p><span class="contact__label">T</span>(55) 5550 1274</p>
      <p><span class="contact__label">E</span>andres.valmar@brovanix.com</p>
      <p>Calle Norte 14. Col. Roma, Mexico DF 06700. MX.</p>
      <p class="contact__web">www.<strong>brovanix</strong>.com</p>
    </div>
  </section>

  <section class="card card--back">
    <div class="back__field" role="img" aria-label="Large brand mark decoration in blue"></div>
    <div class="back__strip">
      <span class="back__name">Brovanix</span>
      <span class="back__tagline">Advanced Cleaning Technologies</span>
    </div>
  </section>
</main>
</body>
</html>
```